Bref créative
Modern Business Name Card for IT Company
qLumio Sdn Bhd
Simple
Marissa Tanaka
Senior Manager
Lot C-17, 5B Floor,
8 Kilner Plaza,
No. 7, Jalan 24/6
47810 Kota Serapi
Seravan, Meridia
marissa@qlumiomarketing.example
www.qlumiomarketing.example
2187605-K
Kindly change the tagline of the website to a different font Segoe UI Semibold since the current font seem to rough and thick. Thanks.

```html
<!DOCTYPE html>
<html lang="en">
<head>
<meta charset="utf-8">
<title>qLumio Stationery</title>
<link href="https://fonts.googleapis.com/css2?family=Exo+2:wght@400;600;700&display=swap" rel="stylesheet">
<style>
  :root {
    --page: #ffffff;
    --paper: #ffffff;
    --blue-deep: #0a2f8f;
    --blue: #1746c2;
    --blue-light: #3d7be0;
    --accent: #2aa7d8;
    --ink: #4a5568;
    --shadow: rgba(20, 30, 60, 0.18);
  }
  * { margin: 0; padding: 0; box-sizing: border-box; }
  html, body { width: 1200px; height: 936px; overflow: hidden; background: var(--page); }
  body { position: relative; font-family: "Exo 2", sans-serif; color: var(--ink); }

  .sheet { position: absolute; background: var(--paper); box-shadow: 0 2px 8px var(--shadow); overflow: hidden; }
  .band { position: absolute; top: 0; bottom: 0; background: linear-gradient(90deg, var(--blue-deep), var(--blue-light) 60%, var(--blue)); }

  .brand { position: absolute; display: flex; align-items: center; gap: 6px; }
  .brand-dot { border-radius: 50%; background: var(--accent); flex: none; }
  .brand-name { font-weight: 700; color: var(--blue); letter-spacing: 0.06em; line-height: 1; }

  .contact { position: absolute; font-size: 6.5px; line-height: 1.45; color: var(--ink); white-space: nowrap; }

  /* Letterhead */
  .letterhead { left: 107px; top: 38px; width: 464px; height: 571px; }
  .letterhead .band { right: 0; width: 18px; }
  .letterhead .brand { left: 30px; top: 70px; }
  .letterhead .brand-dot { width: 9px; height: 9px; }
  .letterhead .brand-name { font-size: 22px; }
  .letterhead .contact { left: 300px; top: 44px; }
  .watermark-circle { position: absolute; left: 48px; top: 228px; width: 74px; height: 74px; border-radius: 50%; background: radial-gradient(circle at 40% 40%, #f1f5fb, #e2e9f5); }

  /* Folder */
  .folder { left: 634px; top: 38px; width: 482px; height: 584px; }
  .folder .band { right: 0; width: 31px; }
  .folder .brand { left: 0; right: 31px; top: 258px; justify-content: center; flex-direction: column; gap: 6px; }
  .folder .brand-dot { width: 20px; height: 20px; }
  .folder .brand-name { font-size: 44px; }

  /* Business cards */
  .card-front { left: 38px; top: 655px; width: 185px; height: 111px; }
  .card-front .band { right: 0; width: 9px; }
  .card-front .brand { left: 10px; top: 12px; gap: 4px; }
  .card-front .brand-dot { width: 6px; height: 6px; }
  .card-front .brand-name { font-size: 15px; }
  .card-front .contact { left: 12px; top: 40px; font-size: 5.5px; }
  .card-front .person { font-weight: 600; color: var(--blue); font-size: 6.5px; }

  .card-back { left: 38px; top: 787px; width: 185px; height: 114px; background: linear-gradient(160deg, var(--blue-light), var(--blue) 55%, var(--blue-deep)); }
  .card-back .web { position: absolute; left: 40px; bottom: 12px; color: #fff; font-size: 5.5px; letter-spacing: 0.06em; font-weight: 600; }

  /* Envelope front */
  .envelope { left: 254px; top: 655px; width: 444px; height: 246px; }
  .envelope .band { right: 0; width: 23px; }
  .envelope .brand { left: 33px; top: 32px; }
  .envelope .brand-dot { width: 8px; height: 8px; }
  .envelope .brand-name { font-size: 20px; }
  .envelope .contact { left: 33px; top: 62px; }
  .band-web { position: absolute; right: 32px; top: 50%; transform: translate(50%, -50%) rotate(-90deg); white-space: nowrap; font-size: 6.5px; letter-spacing: 0.14em; color: var(--blue); font-weight: 600; }

  /* Envelope back */
  .envelope-back { left: 736px; top: 680px; width: 418px; height: 221px; }
  .envelope-back .flap { position: absolute; left: 0; top: 0; width: 100%; height: 62px; background: linear-gradient(90deg, var(--blue-deep), var(--blue-light) 50%, var(--blue-deep)); }
  .envelope-back .web { position: absolute; left: 0; right: 0; top: 24px; text-align: center; color: #fff; font-size: 7.5px; letter-spacing: 0.3em; font-weight: 600; }
  .envelope-back svg { position: absolute; left: 0; top: 62px; }
</style>
</head>
<body>

<section class="sheet letterhead">
  <div class="brand"><span class="brand-dot"></span><span class="brand-name">qLumio</span></div>
  <div class="contact">
    Lot C-17, 5B Floor, 8 Kilner Plaza,<br>
    No. 7, Jalan 24/6, 47810 Kota Serapi<br>
    Seravan, Meridia<br>
    T 000 0000 0000<br>
    marissa@qlumiomarketing.example<br>
    www.qlumiomarketing.example
  </div>
  <div class="watermark-circle"></div>
  <div class="band"></div>
</section>

<section class="sheet folder">
  <div class="brand"><span class="brand-dot"></span><span class="brand-name">qLumio</span></div>
  <div class="band"></div>
</section>

<section class="sheet card-front">
  <div class="brand"><span class="brand-dot"></span><span class="brand-name">qLumio</span></div>
  <div class="contact">
    <span class="person">Marissa Tanaka</span><br>
    Senior Manager<br>
    marissa@qlumiomarketing.example
  </div>
  <div class="band"></div>
</section>

<section class="sheet card-back">
  <div class="web">www.qlumiomarketing.example</div>
</section>

<section class="sheet envelope">
  <div class="brand"><span class="brand-dot"></span><span class="brand-name">qLumio</span></div>
  <div class="contact">
    Lot C-17, 5B Floor, 8 Kilner Plaza,<br>
    No. 7, Jalan 24/6, 47810 Kota Serapi<br>
    Seravan, Meridia
  </div>
  <div class="band-web">www.qlumiomarketing.example</div>
  <div class="band"></div>
</section>

<section class="sheet envelope-back">
  <div class="flap"></div>
  <div class="web">www.qlumiomarketing.example</div>
  <svg width="418" height="159" viewBox="0 0 418 159" aria-hidden="true">
    <path d="M0 159 L170 20 M418 159 L248 20" stroke="#e6e9ef" stroke-width="1" fill="none"/>
  </svg>
</section>

</body>
</html>
```